Large scale additive manufacturing system brochure

Project Title: ORLU Series THERMOPLASTIC EXTRUDER– Product Catalog Design

Description:
We need a professional catalog design for our ORLU Series extruders (ORLU15, ORLU20, ORLU32), which are high-performance extrusion systems for large-scale thermoplastic 3D printing. The catalog should highlight technical specifications, key features, applications, and company profile.

Requirements:
• Clean and modern layout aligned with Tremsol corporate colors
• 10–12 pages including cover, product comparison tables, technical details, and application visuals
• Output capacities should be presented based on PETG +30% GF benchmark
• Integration of company’s partnerships (PELT, ROTH, Zu Forge, Molvet)
• Space for product renders, real application images, and technical drawings
• English text will be provided, but layout and professional design are required

Deliverables:
• Editable source file (InDesign / Illustrator / similar)
• Print-ready PDF version

*i upload the previous catalog, which doesn’t show our vision abd future aim. We need a professional, unique and impressive design.

Target Market(s)

Defense, aerospace, marine, furniture, composite manufacturing

Industry/Entity Type

Robotics and automation

Font styles to use
Sans Serif

Colors

Designer to choose colors to be used in the design.

Requirements
Must have
• High tech impressive view
Nice to have
• Must seen a unique high tech product catalog

```html
<!DOCTYPE html>
<html lang="en">
<head>
<meta charset="utf-8">
<title>Sectors Served</title>
<link href="https://fonts.googleapis.com/css2?family=Arimo:wght@400&display=swap" rel="stylesheet">
<style>
  :root{
    --orange:#de8731;
    --orange-soft:rgba(222,135,49,0);
    --slate:#7c89a9;
    --slate-soft:rgba(124,137,169,0);
    --ink:#111;
    --white:#fff;
    --sky-top:#a2c4da;
    --sky-mid:#3d8db3;
    --sky-low:#98c0d8;
  }
  *{margin:0;padding:0;box-sizing:border-box}
  html,body{width:848px;height:1200px;overflow:hidden}
  body{font-family:"Arimo",Arial,sans-serif;color:var(--ink)}
  .page{position:relative;width:848px;height:1200px;overflow:hidden;
    background:linear-gradient(180deg,var(--sky-top) 0%,#7fb0cd 25%,var(--sky-mid) 50%,#68a6c7 68%,var(--sky-low) 88%,var(--sky-low) 100%)}
  .page-title{position:absolute;left:77px;top:22px;font-size:36px;font-weight:400;letter-spacing:.3px;line-height:1}
  .band{position:absolute}
  .band--right{clip-path:polygon(0 0,calc(100% - 41px) 0,100% 50%,calc(100% - 41px) 100%,0 100%)}
  .band--left{clip-path:polygon(65px 0,100% 0,100% 100%,65px 100%,0 50%)}
  .band--right.band--slate{background:linear-gradient(90deg,var(--slate-soft) 0%,rgba(124,137,169,.55) 35%,var(--slate) 75%)}
  .band--right.band--orange{background:linear-gradient(90deg,var(--orange-soft) 0%,rgba(222,135,49,.45) 40%,var(--orange) 85%)}
  .band--left.band--orange{background:linear-gradient(90deg,var(--orange) 0%,rgba(222,135,49,.6) 45%,var(--orange-soft) 100%)}
  .band--left.band--slate{background:linear-gradient(90deg,var(--slate) 0%,rgba(124,137,169,.75) 50%,var(--slate-soft) 100%)}
  .tab{position:absolute;height:50px;display:flex;align-items:center;justify-content:center;
    clip-path:polygon(0 0,91% 0,100% 100%,9% 100%);color:var(--white);font-size:25px;line-height:1}
  .tab--orange{background:var(--orange)}
  .tab--slate{background:var(--slate)}
  .tab--two-line{flex-direction:column;align-items:flex-start;font-size:24px;line-height:.95;padding-left:36px}
  .tab--two-line span:last-child{padding-left:68px}
  .copy{position:absolute;font-size:18.8px;line-height:24px}
  .photo{position:absolute;left:0;top:510px;width:264px;height:552px;
    background:linear-gradient(160deg,#e9eaeb 0%,#d8d6d2 30%,#c96f3d 42%,#b9b6b1 55%,#efefee 75%,#cfcdca 100%)}
  .sector-icons{position:absolute;left:0;top:0}
</style>
</head>
<body>
<main class="page">
  <h1 class="page-title">SECTORS SERVED</h1>

  <svg class="sector-icons" width="848" height="400" viewBox="0 0 848 400" aria-hidden="true">
    <g fill="none" stroke="#000" stroke-width="1.2">
      <polygon points="694,81 831,200 699,351 562,233"/>
      <line x1="628" y1="157" x2="765" y2="276"/>
      <line x1="762" y1="141" x2="631" y2="292"/>
    </g>
    <g fill="#111">
      <!-- factory -->
      <path d="M662 150 L662 165 L724 165 L724 155 L718 155 L718 130 L712 130 L712 150 L700 143 L700 150 L688 143 L688 150 L676 143 L676 150 Z"/>
      <!-- plane -->
      <g transform="translate(763 204) rotate(45)">
        <path d="M-3 -34 Q0 -38 3 -34 L3 -6 L26 6 L26 11 L3 4 L3 22 L11 28 L11 32 L0 29 L-11 32 L-11 28 L-3 22 L-3 4 L-26 11 L-26 6 L-3 -6 Z"/>
      </g>
      <!-- car -->
      <path d="M592 238 Q590 222 600 218 L612 207 Q624 203 636 207 L648 217 Q657 220 657 232 L657 238 Z"/>
      <circle cx="603" cy="238" r="6"/><circle cx="646" cy="238" r="6"/>
      <!-- anchor -->
      <g fill="none" stroke="#111" stroke-width="4" stroke-linecap="round">
        <circle cx="689" cy="250" r="5"/>
        <line x1="689" y1="255" x2="689" y2="305"/>
        <line x1="673" y1="263" x2="705" y2="263"/>
        <path d="M666 285 Q670 305 689 305 Q708 305 712 285"/>
      </g>
    </g>
  </svg>

  <!-- Defense -->
  <div class="band band--right band--slate" style="left:0;top:102px;width:618px;height:101px"></div>
  <div class="tab tab--orange" style="left:155px;top:71px;width:245px">DEFENSE</div>
  <p class="copy" style="left:77px;top:120px;width:500px">Rapid prototyping of housings and enclosures, low-volume tooling, jigs &amp; fixtures, composite mold masters (non-ITAR production support).</p>

  <!-- Aerospace -->
  <div class="band band--right band--orange" style="left:0;top:246px;width:607px;height:100px"></div>
  <div class="tab tab--slate" style="left:218px;top:219px;width:244px">AEROSPACE</div>
  <p class="copy" style="left:79px;top:273px;width:480px">Layup tools, vacuum form tools, drill jigs, non-flight composite tooling, aerodynamic mockups and form/fit prototypes.</p>

  <!-- Marine -->
  <div class="band band--right band--slate" style="left:0;top:380px;width:618px;height:101px"></div>
  <div class="tab tab--orange" style="left:301px;top:353px;width:245px">MARINE</div>
  <p class="copy" style="left:79px;top:407px;width:500px">Hull sections, fairings, cores, custom molds; corrosion-resistant materials for marine environments.</p>

  <div class="photo" role="img" aria-label="Photo of a robotic arm with a large-format extruder printing a curved white thermoplastic panel in a workshop"></div>

  <!-- Furniture -->
  <div class="band band--left band--orange" style="left:276px;top:535px;width:540px;height:100px"></div>
  <div class="tab tab--slate" style="left:398px;top:499px;width:244px">FURNITURE</div>
  <p class="copy" style="left:341px;top:547px;width:440px">Large sculptural shells, ergonomic forms, upholstery molds, custom fixtures for production lines.</p>

  <!-- Interior design -->
  <div class="band band--left band--slate" style="left:281px;top:672px;width:535px;height:100px"></div>
  <div class="tab tab--orange tab--two-line" style="left:448px;top:643px;width:243px"><span>INTERIOR</span><span>DESIGN</span></div>
  <p class="copy" style="left:324px;top:698px;width:480px">Parametric panels, bespoke décor, lighting housings, architectural elements with complex geometry.</p>

  <!-- Automotive -->
  <div class="band band--left band--orange" style="left:272px;top:806px;width:544px;height:101px"></div>
  <div class="tab tab--slate" style="left:448px;top:781px;width:244px">AUTOMOTIVE</div>
  <p class="copy" style="left:341px;top:832px;width:470px">Prototype body panels, bumpers, fixtures, composite tooling, assembly aids.</p>

  <!-- Construction / Architecture -->
  <div class="band band--left band--slate" style="left:277px;top:960px;width:539px;height:101px"></div>
  <div class="tab tab--orange tab--two-line" style="left:357px;top:923px;width:306px;padding-left:30px"><span>CONSTRUCTION/</span><span>ARCHITECTURE</span></div>
  <p class="copy" style="left:333px;top:984px;width:440px">Façade panels, molds for casting, large-format functional components.</p>
</main>
</body>
</html>
```